Web design for Digital Marketing Agency

Hello,
the name of our agency is "Bright Lantern" with the idea that we make Bright Lantern for our client count. You can find our logo attached. Use blue tone similar to it a modern sans serif form that fits the design.
We need a web design similar to this one:
https: // larkfield-studio. de /
What I like about this design:
- clear navigation with personalized Pic for phone number and clear call to action in nav bar (which is then repeated in hero image)
- the hero image having custom cartoon represtation giving a visual impression of what the company does (in our case paid adwords on different channels, like Wexly Ads, Tribbon etc; and analyzing data and optimizing the website based on that)
-a clear cut structure that goes on with similar cartoons when appropriate
- using bright background colors for sections
- lots of space so content can breath
The following sections are needed in this order:
-navbar
-hero image with text:
"Digital marketing for companies who know that Bright Lantern counts.
We always help you to achieve the best in every digital transaction. Because like in real life, you don't get a second channel for your first impression. "
Services Section:
1.) Paid advertising
2.) Analytics & Optimization
3.) Chatbots
4.) E-commerce shops
-Explaining the Service Secion (the section explaining the service that is chose by the user above 1/3 image / 2/3 text - image should also be a cartoon fitting in style to overall pic and representing the service that will be explained)
- Bright Lantern Concept
2 rings similar to above website
- the process section
- what customer are saying section
-contact form section
-footer
Target Market(s)
Companies seeking to increase sales online / generate new lead online. Main focus ecommerce but also traditional companies like real estate or lawyers
Number of Pages Required
1 page
Font styles to use
Look and feel
Each slider illustrates characteristics of the customer's brand and the style your logo design should communicate.

```html
<!DOCTYPE html>
<html lang="en">
<head>
<meta charset="utf-8">
<title>Bright Lantern – Digital Marketing</title>
<link href="https://fonts.googleapis.com/css2?family=Poppins:wght@400;500;600;700;800&display=swap" rel="stylesheet">
<style>
:root{
  --blue:#2a9fd8;
  --blue-dark:#1c7fb6;
  --sky:#e6f4fc;
  --sky-2:#cfe9f8;
  --ink:#1f2a37;
  --muted:#6b7785;
  --line:#e3e8ee;
  --pink:#e43bc3;
  --green:#7dc242;
  --cobalt:#2f8fe0;
  --orange:#f39a2b;
  --navy:#0f2a44;
  --navy-2:#0a1f33;
  --white:#ffffff;
}
*{box-sizing:border-box;margin:0;padding:0}
html,body{width:1200px;height:2444px;overflow:hidden}
body{font-family:"Poppins",Arial,sans-serif;color:var(--ink);background:var(--white);position:relative}
.abs{position:absolute}
h2.section-title{position:absolute;left:0;width:1200px;text-align:center;font-size:26px;font-weight:700;letter-spacing:1px;color:var(--ink);z-index:1}
.btn{display:inline-block;background:var(--blue);color:var(--white);font-size:12px;font-weight:600;padding:10px 20px;border-radius:4px}
.btn-outline{border:1.5px solid var(--blue);color:var(--blue);background:transparent;font-size:11px;padding:7px 14px;border-radius:4px;font-weight:600}

/* nav */
.site-nav{position:absolute;top:0;left:0;width:1200px;height:64px;display:flex;align-items:center;padding:0 56px;z-index:2}
.brand{display:flex;align-items:center;gap:8px;font-weight:700;font-size:15px;color:var(--blue);letter-spacing:.5px}
.brand-dot{width:30px;height:30px;border-radius:50%;background:var(--blue)}
.nav-links{display:flex;gap:28px;margin-left:auto;font-size:12px;color:var(--ink)}
.nav-phone{display:flex;align-items:center;gap:6px;margin-left:40px;font-size:12px;font-weight:600;color:var(--blue)}
.nav-cta{margin-left:22px}

/* hero */
.hero-bg{left:0;top:0;width:1200px;height:520px}
.hero-copy{left:300px;top:96px;width:600px;text-align:center}
.hero-copy h1{font-size:38px;font-weight:800;color:var(--ink);letter-spacing:1px;line-height:1.1}
.hero-copy .sub{font-size:17px;font-weight:700;margin-top:8px;line-height:1.3}
.hero-copy p{font-size:11px;color:var(--muted);margin:14px auto 0;width:420px;line-height:1.6}
.hero-copy .btn{margin-top:60px}
.hero-art-left{left:0;top:150px;width:330px;height:320px;border-radius:0 160px 160px 0;background:linear-gradient(135deg,#bfe3f7,#7cc5ec)}
.hero-art-right{left:950px;top:330px;width:220px;height:170px;border-radius:110px 110px 20px 20px;background:linear-gradient(135deg,#d5edfa,#8fcdef)}

/* services */
.services{left:220px;top:620px;width:760px;display:flex;gap:20px}
.service-card{width:175px;height:280px;border-radius:10px;padding:14px;color:var(--white);box-shadow:0 8px 18px rgba(30,60,90,.15);position:relative}
.service-card .art{height:70px;border-radius:6px;background:rgba(255,255,255,.28);margin:-40px 10px 12px}
.service-card h3{font-size:11px;font-weight:700;text-align:center;letter-spacing:.5px;margin-bottom:10px}
.service-card p{font-size:9.5px;line-height:1.55;opacity:.95}
.service-card .more{position:absolute;left:50%;bottom:16px;transform:translateX(-50%);font-size:9px;border:1px solid var(--white);border-radius:3px;padding:4px 12px}
.c-pink{background:var(--pink)} .c-green{background:var(--green)} .c-blue{background:var(--cobalt)} .c-orange{background:var(--orange)}

/* concept */
.concept-copy{left:220px;top:1010px;width:300px}
.concept-copy h3{font-size:14px;font-weight:700;margin-bottom:12px}
.concept-copy p{font-size:10.5px;color:var(--muted);line-height:1.6;margin-bottom:10px}
.concept-copy .btn{margin-top:8px;font-size:11px;padding:8px 16px}
.venn{left:580px;top:960px}

/* process */
.steps{left:200px;top:1366px;width:800px;display:flex;justify-content:space-between}
.step{width:230px;text-align:center}
.step h4{font-size:12px;font-weight:700;margin-top:8px}
.step p{font-size:9.5px;color:var(--muted);line-height:1.5;margin-top:4px}
.step-icon{width:44px;height:44px;margin:0 auto}

/* testimonials */
.testimonials{left:248px;top:1580px;width:712px;display:flex;gap:16px}
.t-card{width:166px;height:256px;background:var(--white);border-radius:6px;box-shadow:0 4px 16px rgba(30,60,90,.12);overflow:hidden}
.t-photo{height:88px;background:linear-gradient(135deg,#8a9aa8,#4b5a68)}
.t-body{padding:12px}
.t-role{font-size:9px;font-weight:700;color:var(--blue);text-transform:uppercase;margin-bottom:6px}
.t-body p{font-size:9px;color:var(--muted);line-height:1.55}
.t-foot{display:flex;justify-content:space-between;font-size:8.5px;margin-top:14px;color:var(--ink);font-weight:600}
.dots{left:0;width:1200px;top:1848px;display:flex;justify-content:center;gap:8px}
.dots span{width:8px;height:8px;border-radius:50%;background:var(--sky-2)}
.dots span.on{background:var(--blue)}
.arrow{top:1698px;width:26px;height:26px;border-radius:50%;border:1px solid var(--line);display:flex;align-items:center;justify-content:center;color:var(--muted);font-size:13px}

/* contact */
.contact-copy{left:220px;top:1970px;width:420px}
.contact-copy h3{font-size:14px;font-weight:700;line-height:1.3}
.contact-copy .lead{font-size:10px;color:var(--muted);margin-top:8px;line-height:1.5}
.tick-list{list-style:none;margin-top:16px}
.tick-list li{display:flex;gap:10px;font-size:10px;color:var(--muted);line-height:1.5;margin-bottom:14px}
.tick-list svg{flex:none;margin-top:2px}
.contact-form{left:680px;top:1990px;width:270px;background:var(--white);border-radius:8px;box-shadow:0 6px 24px rgba(30,60,90,.14);padding:20px}
.field{height:24px;border:1px solid var(--line);border-radius:3px;margin-bottom:10px;font-size:9px;color:#a0aab4;padding:5px 8px}
.field.area{height:56px}
.contact-form .btn{font-size:10px;padding:7px 18px}
.contact-art{left:880px;top:1950px;width:120px;height:240px;border-radius:60px;background:linear-gradient(180deg,#d7eefb,#a3d6f2)}

/* footer */
.site-footer{left:0;top:2260px;width:1200px;height:184px;background:var(--navy);color:#c9d6e3}
.footer-brand{position:absolute;top:14px;left:0;width:1200px;display:flex;justify-content:center}
.footer-brand .brand{color:var(--white);font-size:13px}
.footer-brand .brand-dot{width:24px;height:24px}
.f-col{position:absolute;top:58px;font-size:9.5px;line-height:1.8}
.f-col h5{color:var(--white);font-size:11px;font-weight:600;margin-bottom:4px}
.sub-row{display:flex;margin-top:4px}
.sub-row .in{width:150px;height:24px;background:var(--white);border-radius:3px 0 0 3px;color:#99a;font-size:9px;padding:5px 8px}
.sub-row .go{height:24px;background:var(--blue);color:var(--white);font-size:9px;padding:5px 10px;border-radius:0 3px 3px 0}
.socials{display:flex;gap:8px;margin-top:10px}
.socials span{width:18px;height:18px;border-radius:50%;background:#2b4a68}
.footer-bar{position:absolute;bottom:0;left:0;width:1200px;height:30px;background:var(--navy-2);display:flex;align-items:center;justify-content:space-between;padding:0 60px;font-size:9px;color:#8ea3b8}
</style>
</head>
<body>

<svg class="abs hero-bg" viewBox="0 0 1200 520" aria-hidden="true">
  <path d="M0 0H1200V380C1080 470 960 420 820 460C650 510 520 430 360 470C220 505 100 470 0 500Z" fill="#eef7fd"/>
  <path d="M0 420C120 380 220 440 360 420C520 395 640 470 820 430C960 400 1080 440 1200 400V470C1080 500 960 460 820 490C650 520 520 470 360 500C220 520 100 490 0 510Z" fill="#d9eef9"/>
</svg>

<header class="site-nav">
  <div class="brand"><span class="brand-dot"></span>BRIGHT LANTERN</div>
  <nav class="nav-links"><span>Home</span><span>About</span><span>Services</span><span>Testimonials</span><span>Contact</span></nav>
  <div class="nav-phone">
    <svg width="14" height="14" viewBox="0 0 24 24"><path d="M6.6 10.8a15 15 0 006.6 6.6l2.2-2.2a1 1 0 011-.25 11.4 11.4 0 003.6.6 1 1 0 011 1V20a1 1 0 01-1 1A17 17 0 013 4a1 1 0 011-1h3.5a1 1 0 011 1c0 1.25.2 2.45.6 3.6a1 1 0 01-.25 1z" fill="#2a9fd8"/></svg>
    040 555 0187
  </div>
  <span class="btn-outline nav-cta">Free Consultation</span>
</header>

<div class="abs hero-art-left" role="img" aria-label="Cartoon of marketers working with ad channels, charts and devices"></div>
<div class="abs hero-art-right" role="img" aria-label="Cartoon of a person analysing website data on a laptop"></div>

<section class="abs hero-copy">
  <h1>DIGITAL MARKETING</h1>
  <div class="sub">FOR COMPANIES WHO KNOW<br>THAT BRIGHT LANTERN COUNTS</div>
  <p>We always help you to achieve the best in every digital transaction. Because like in real life, you don't get a second channel for your first impression.</p>
  <span class="btn">Free Consultation</span>
</section>

<h2 class="section-title" style="top:552px">OUR SERVICES</h2>
<section class="abs services">
  <article class="service-card c-pink">
    <div class="art" role="img" aria-label="Illustration of paid advertising"></div>
    <h3>PAID ADVERTISING</h3>
    <p>We plan and run paid campaigns on Wexly Ads, Tribbon and other channels, so every budget reaches buyers who are ready to act and your cost per lead stays low.</p>
    <span class="more">Read more</span>
  </article>
  <article class="service-card c-green">
    <div class="art" role="img" aria-label="Illustration of analytics dashboards"></div>
    <h3>ANALYTICS &amp; OPTIMIZATION</h3>
    <p>We track what visitors do, find where they drop off and test changes to your website, so more of your traffic turns into enquiries and sales every month.</p>
    <span class="more">Read more</span>
  </article>
  <article class="service-card c-blue">
    <div class="art" role="img" aria-label="Illustration of a chatbot conversation"></div>
    <h3>CHATBOTS</h3>
    <p>Smart chatbots answer questions day and night, qualify leads and pass warm contacts to your team, so no visitor leaves your page without help.</p>
    <span class="more">Read more</span>
  </article>
  <article class="service-card c-orange">
    <div class="art" role="img" aria-label="Illustration of an online shop"></div>
    <h3>E-COMMERCE SHOPS</h3>
    <p>We build fast, clear online shops with simple checkouts and product pages that sell, ready to connect with your ads and your analytics from day one.</p>
    <span class="more">Read more</span>
  </article>
</section>

<h2 class="section-title" style="top:906px">OUR CONCEPT</h2>
<section class="abs concept-copy">
  <h3>Online marketing that will grow your business</h3>
  <p>Through the interaction of qualified traffic and landing pages that are optimised in terms of conversions, we can achieve previously unimagined results.</p>
  <p>Our focus is performance for your company. We create practical strategies that fit your market and deliver clear numbers.</p>
  <span class="btn">Arrange Consultation</span>
</section>
<svg class="abs venn" width="440" height="290" viewBox="0 0 440 290" aria-label="Traffic and conversion diagram">
  <circle cx="145" cy="145" r="132" fill="#5ab4e4" opacity=".75"/>
  <circle cx="295" cy="145" r="132" fill="#a9d8f2" opacity=".7"/>
  <text x="95" y="151" font-family="Poppins,sans-serif" font-size="16" font-weight="700" fill="#0f2a44" text-anchor="middle">TRAFFIC</text>
  <text x="345" y="151" font-family="Poppins,sans-serif" font-size="16" font-weight="700" fill="#0f2a44" text-anchor="middle">CONVERSION</text>
</svg>

<h2 class="section-title" style="top:1300px">HOW IT WORKS</h2>
<svg class="abs" style="left:320px;top:1376px" width="560" height="20" aria-hidden="true"><line x1="0" y1="10" x2="560" y2="10" stroke="#b8cbd9" stroke-dasharray="5 5"/></svg>
<section class="abs steps">
  <div class="step">
    <svg class="step-icon" viewBox="0 0 44 44"><rect x="9" y="6" width="26" height="32" rx="3" fill="#fff" stroke="#6b7785" stroke-width="2"/><line x1="15" y1="16" x2="29" y2="16" stroke="#6b7785" stroke-width="2"/><line x1="15" y1="23" x2="29" y2="23" stroke="#6b7785" stroke-width="2"/><line x1="15" y1="30" x2="24" y2="30" stroke="#6b7785" stroke-width="2"/></svg>
    <h4>An incredible offer</h4>
    <p>We tailor a plan to your goals and your budget, with clear steps and fair prices.</p>
  </div>
  <div class="step">
    <svg class="step-icon" viewBox="0 0 44 44"><circle cx="16" cy="15" r="6" fill="#fff" stroke="#6b7785" stroke-width="2"/><circle cx="30" cy="15" r="6" fill="#fff" stroke="#6b7785" stroke-width="2"/><path d="M5 36c0-7 5-11 11-11s11 4 11 11M22 28c2-2 5-3 8-3 6 0 10 4 10 11" fill="none" stroke="#6b7785" stroke-width="2"/></svg>
    <h4>Entrepreneurial with sincere customers</h4>
    <p>We work side by side with you and share every result openly along the way.</p>
  </div>
  <div class="step">
    <svg class="step-icon" viewBox="0 0 44 44"><polyline points="6,34 16,22 24,28 38,10" fill="none" stroke="#6b7785" stroke-width="2"/><polyline points="30,10 38,10 38,18" fill="none" stroke="#6b7785" stroke-width="2"/></svg>
    <h4>Data-driven optimisation</h4>
    <p>We measure, learn and refine your campaigns so growth keeps building month after month.</p>
  </div>
</section>

<h2 class="section-title" style="top:1520px">CLIENT TESTIMONIALS</h2>
<div class="abs arrow" style="left:212px">‹</div>
<div class="abs arrow" style="left:962px">›</div>
<section class="abs testimonials">
  <article class="t-card">
    <div class="t-photo" role="img" aria-label="Portrait photo of a client"></div>
    <div class="t-body"><div class="t-role">E-commerce owner</div>
      <p>Our online sales doubled within six months. The team explains every step and always finds new ways to improve our ads.</p>
      <div class="t-foot"><span>Mara Lindqvist</span><span>★★★★★</span></div></div>
  </article>
  <article class="t-card">
    <div class="t-photo" role="img" aria-label="Portrait photo of a client"></div>
    <div class="t-body"><div class="t-role">Real estate agent</div>
      <p>We now get steady, qualified leads every week. The landing pages convert far better than anything we had before.</p>
      <div class="t-foot"><span>Tomas Reyes</span><span>★★★★★</span></div></div>
  </article>
  <article class="t-card">
    <div class="t-photo" role="img" aria-label="Portrait photo of a client"></div>
    <div class="t-body"><div class="t-role">Law firm partner</div>
      <p>Clear reports, honest advice and real results. Our chatbot now books first meetings while we focus on clients.</p>
      <div class="t-foot"><span>Ines Varga</span><span>★★★★★</span></div></div>
  </article>
  <article class="t-card">
    <div class="t-photo" role="img" aria-label="Portrait photo of a client"></div>
    <div class="t-body"><div class="t-role">Shop founder</div>
      <p>They rebuilt our shop and checkout. Fewer abandoned carts, more repeat buyers and a much better cost per sale.</p>
      <div class="t-foot"><span>Owen Blake</span><span>★★★★★</span></div></div>
  </article>
</section>
<div class="abs dots"><span></span><span class="on"></span><span></span><span></span></div>

<h2 class="section-title" style="top:1912px">CONTACT US</h2>
<section class="abs contact-copy">
  <h3>We will contact you as soon as possible.</h3>
  <p class="lead">We look forward to all of your questions about our services – you'll be the first on the right list.</p>
  <ul class="tick-list">
    <li><svg width="14" height="14" viewBox="0 0 14 14"><circle cx="7" cy="7" r="7" fill="#2a9fd8"/><polyline points="4,7 6,9.5 10,4.5" fill="none" stroke="#fff" stroke-width="1.6"/></svg>Personal consultation with better, more digitally effective customers and employees.</li>
    <li><svg width="14" height="14" viewBox="0 0 14 14"><circle cx="7" cy="7" r="7" fill="#2a9fd8"/><polyline points="4,7 6,9.5 10,4.5" fill="none" stroke="#fff" stroke-width="1.6"/></svg>How you can achieve measurable results through targeted online marketing that supports your corporate goals.</li>
    <li><svg width="14" height="14" viewBox="0 0 14 14"><circle cx="7" cy="7" r="7" fill="#2a9fd8"/><polyline points="4,7 6,9.5 10,4.5" fill="none" stroke="#fff" stroke-width="1.6"/></svg>Concrete strategy that makes your company competitive for your target customers online.</li>
  </ul>
</section>
<div class="abs contact-art" role="img" aria-label="Cartoon of a person sending a message"></div>
<form class="abs contact-form">
  <div class="field">Name</div>
  <div class="field">Email</div>
  <div class="field">Phone</div>
  <div class="field area">Message</div>
  <span class="btn">Send</span>
</form>

<footer class="abs site-footer">
  <div class="footer-brand"><div class="brand"><span class="brand-dot"></span>BRIGHT LANTERN</div></div>
  <div class="f-col" style="left:60px"><h5>Quick Links</h5>Home<br>About<br>Services<br>Testimonials<br>Contact</div>
  <div class="f-col" style="left:330px"><h5>Contact Us</h5>Phone number<br>040 555 0187<br>Email<br>hello@brightlantern.example</div>
  <div class="f-col" style="left:640px"><h5>Subscribe to our Newsletter</h5>
    <div class="sub-row"><span class="in">Email Address</span><span class="go">Subscribe</span></div>
    <div class="socials"><span></span><span></span><span></span><span></span></div>
  </div>
  <div class="footer-bar"><span>Privacy Policy · Terms of Use</span><span>© Bright Lantern. All rights reserved.</span></div>
</footer>

</body>
</html>
```